Halvery Building Group Website

Need a dynamic corporate website that can be built on with time. We want to get our information out to the world and have a place where customers can submit requests for proposals.

Target Market(s)

Custom home owners and buyers. Architects and Real Estate Agents.

Industry/Entity Type

Construction

Number of Pages Required

3 page

Font styles to use
Serif
Sans Serif

Requirements
Must have
• Company logo, about, company contact information, biography, contact, projects,
• Sleek, modern, clean, attractive design.
• Online form customers can use for filling out a request for project proposal.
• Workcircle hyperlink.
• Uses www.halverybuildinggroup.example

```html
<!DOCTYPE html>
<html lang="en">
<head>
<meta charset="utf-8">
<title>Halvery Building Group</title>
<link rel="stylesheet" href="https://fonts.googleapis.com/css2?family=Raleway:wght@400;500;600;700&family=Open+Sans:wght@400;600;700&display=swap">
<style>
  :root {
    --brand-blue: #0b56a3;
    --sky-blue: #36a3d9;
    --ink: #3a3a3a;
    --muted: #5f5f5f;
    --panel: #f2f2f2;
    --footer: #2b2a72;
    --white: #ffffff;
  }
  * { margin: 0; padding: 0; box-sizing: border-box; }
  html, body { width: 699px; height: 1200px; overflow: hidden; background: var(--white); }
  body { position: relative; font-family: "Open Sans", Arial, sans-serif; }
  .abs { position: absolute; }
  a { text-decoration: none; }

  .hero { left: 0; top: 0; width: 699px; height: 376px;
    background: linear-gradient(180deg, #e6edf3 0%, #d7dfe6 40%, #b9bcc0 70%, #9a9c9f 100%); }
  .hero-light { left: 0; top: 0; width: 699px; height: 376px;
    background: radial-gradient(circle at 92% 18%, rgba(255,250,230,.95) 0%, rgba(255,250,230,0) 40%),
                linear-gradient(180deg, rgba(255,255,255,0) 50%, rgba(110,110,115,.35) 100%); }
  .brand-mark { left: 306px; top: 66px; width: 56px; height: 56px; background: var(--brand-blue); }
  .brand-name { left: 0; top: 136px; width: 699px; text-align: center;
    font-family: "Raleway", Arial, sans-serif; font-weight: 700; font-size: 56px;
    letter-spacing: 3px; line-height: 66px; color: var(--brand-blue); }
  .brand-sub { left: 0; top: 204px; width: 699px; text-align: center;
    font-family: "Raleway", Arial, sans-serif; font-weight: 600; font-size: 22px;
    letter-spacing: 1.5px; line-height: 28px; color: var(--ink); }
  .rule { top: 188px; height: 1px; background: #222; }
  .rule-dot { top: 185px; width: 7px; height: 7px; border-radius: 50%; background: #111; }

  .main-nav { left: 0; top: 376px; width: 699px; height: 34px; background: var(--brand-blue); }
  .nav-item { top: 0; height: 34px; line-height: 34px; font-family: "Raleway", Arial, sans-serif;
    font-size: 12.5px; color: var(--white); text-align: center; }
  .nav-item.is-active { background: var(--sky-blue); }

  .welcome-kicker { left: 0; top: 452px; width: 699px; text-align: center;
    font-family: "Raleway", Arial, sans-serif; font-size: 20px; line-height: 24px; color: var(--muted); }
  .welcome-title { left: 0; top: 478px; width: 699px; text-align: center;
    font-family: "Raleway", Arial, sans-serif; font-weight: 400; font-size: 29.5px; line-height: 36px; color: var(--brand-blue); }
  .welcome-copy { left: 86px; top: 533px; width: 530px; text-align: center;
    font-size: 9.3px; line-height: 14.6px; color: var(--muted); }

  .projects { left: 0; top: 668px; width: 699px; height: 417px; background: var(--panel); }
  .projects-title { left: 0; top: 700px; width: 699px; text-align: center;
    font-family: "Raleway", Arial, sans-serif; font-weight: 400; font-size: 30px; line-height: 38px; }
  .projects-title .light { color: var(--sky-blue); }
  .projects-title .deep { color: var(--brand-blue); }
  .view-all { left: 298px; top: 1014px; width: 121px; height: 30px; border-radius: 15px;
    background: var(--sky-blue); box-shadow: 2px 3px 3px rgba(0,0,0,.35);
    text-align: center; line-height: 30px; font-family: "Raleway", Arial, sans-serif;
    font-size: 13px; color: #1c2c4a; }

  .site-footer { left: 0; top: 1085px; width: 699px; height: 115px; background: var(--footer); }
  .footer-link { top: 1098px; font-size: 11.5px; color: #e4e4f0; }
  .social { top: 1097px; width: 24px; height: 24px; border: 1px solid #9ea0d0; }
  .social.is-filled { background: var(--sky-blue); border-color: var(--sky-blue); }
  .footer-divider { left: 45px; top: 1129px; width: 609px; height: 1px; background: #4a4a8e; }
  .contact-label { font-size: 8px; font-weight: 700; color: var(--white); }
  .contact-text { font-size: 8.5px; color: #e8e8f4; }
  .copyright { left: 0; top: 1180px; width: 699px; text-align: center; font-size: 8.5px; color: #e8e8f4; }
  .copyright strong { color: var(--sky-blue); font-weight: 600; }
</style>
</head>
<body>

<header>
  <div class="abs hero" role="img" aria-label="Sunlit city skyline of high-rise towers"></div>
  <div class="abs hero-light"></div>
  <div class="abs brand-mark"></div>
  <div class="abs brand-name">HALVERY</div>
  <div class="abs rule" style="left:45px;width:88px"></div>
  <div class="abs rule-dot" style="left:130px"></div>
  <div class="abs rule-dot" style="left:563px"></div>
  <div class="abs rule" style="left:568px;width:87px"></div>
  <div class="abs brand-sub">HALVERY BUILDING GROUP, INC.</div>

  <nav class="abs main-nav">
    <a class="abs nav-item is-active" style="left:102px;width:83px">HOME</a>
    <a class="abs nav-item" style="left:200px;width:70px">ABOUT</a>
    <a class="abs nav-item" style="left:298px;width:74px">PROJECT</a>
    <a class="abs nav-item" style="left:402px;width:76px">CONTACT</a>
  </nav>
</header>

<main>
  <div class="abs welcome-kicker">WELCOME TO</div>
  <h1 class="abs welcome-title">HALVERY BUILDING GROUP</h1>
  <p class="abs welcome-copy">Lorem Ipsum is simply dummy text of the printing and typesetting industry. Lorem Ipsum has been the industry's standard dummy text ever since the 1500s, when an unknown printer took a galley of type and scrambled it to make a type specimen book. It has survived not only five centuries, but also the leap into electronic typesetting, remaining essentially unchanged. It was popularised in the 1960s with the release of Presstype sheets containing Lorem Ipsum passages, and more recently with desktop publishing software like Layoutwright including versions of Lorem Ipsum.</p>

  <section class="abs projects"></section>
  <h2 class="abs projects-title"><span class="light">Our</span> <span class="deep">Projects</span></h2>

  <div class="abs" style="left:45px;top:770px;width:148px;height:92px;background:linear-gradient(135deg,#e4e4e0,#c9a85a 55%,#d8d8d4)" role="img" aria-label="Cutaway model of a house on plans"></div>
  <div class="abs" style="left:45px;top:867px;width:148px;height:122px;background:linear-gradient(180deg,#8fb0d8,#9a8e84 45%,#5d5a55)" role="img" aria-label="Row of new townhouses"></div>
  <div class="abs" style="left:198px;top:770px;width:148px;height:134px;background:linear-gradient(180deg,#e8ecd8,#b7d24a 45%,#eef2e4)" role="img" aria-label="Modern lime-green interior lounge"></div>
  <div class="abs" style="left:198px;top:910px;width:148px;height:79px;background:linear-gradient(180deg,#f4f6f6,#dfe6e2)" role="img" aria-label="Bright white open-plan interior"></div>
  <div class="abs" style="left:353px;top:770px;width:148px;height:79px;background:linear-gradient(135deg,#7a5a3c,#c7a47a 55%,#e6dcc8)" role="img" aria-label="Warm living room interior"></div>
  <div class="abs" style="left:353px;top:855px;width:148px;height:134px;background:linear-gradient(180deg,#8f9aa4,#d8d0a0 50%,#6a6e60)" role="img" aria-label="Site workers reviewing building plans"></div>
  <div class="abs" style="left:506px;top:770px;width:148px;height:122px;background:linear-gradient(180deg,#4f8fd6,#9cc0e2 45%,#3e4a3a)" role="img" aria-label="Glass-domed building with palm trees"></div>
  <div class="abs" style="left:506px;top:898px;width:148px;height:91px;background:linear-gradient(135deg,#3a3f4c,#b8aea2 55%,#4a6ad0)" role="img" aria-label="Reception desk with blue lighting"></div>

  <a class="abs view-all">VIEW ALL</a>
</main>

<footer>
  <div class="abs site-footer"></div>
  <a class="abs footer-link" style="left:46px">Home</a>
  <a class="abs footer-link" style="left:105px">About</a>
  <a class="abs footer-link" style="left:165px">Projects</a>
  <a class="abs footer-link" style="left:231px">Contact</a>

  <a class="abs social is-filled" style="left:569px" aria-label="Friendnest"></a>
  <a class="abs social" style="left:599px" aria-label="Chirpline"></a>
  <a class="abs social" style="left:630px" aria-label="Workcircle"></a>

  <div class="abs footer-divider"></div>

  <svg class="abs" style="left:45px;top:1143px" width="14" height="17" viewBox="0 0 14 17" aria-hidden="true">
    <rect x="6" y="0" width="2" height="17" fill="#fff"/>
    <rect x="1" y="3" width="12" height="3" fill="#fff"/>
    <rect x="1" y="8" width="12" height="3" fill="#fff"/>
  </svg>
  <div class="abs contact-label" style="left:66px;top:1142px">POSTAL ADDRESS</div>
  <div class="abs contact-text" style="left:66px;top:1155px">123 Building Name, City, Country - zipcode</div>

  <svg class="abs" style="left:338px;top:1146px" width="14" height="14" viewBox="0 0 14 14" aria-hidden="true">
    <path d="M3 1 L5.5 3.5 L4 5.5 C5 7.5 6.5 9 8.5 10 L10.5 8.5 L13 11 L11 13 C6 12.5 1.5 8 1 3 Z" fill="none" stroke="#fff" stroke-width="1"/>
  </svg>
  <div class="abs contact-text" style="left:358px;top:1147px">(456) 555 0142</div>

  <svg class="abs" style="left:505px;top:1147px" width="16" height="12" viewBox="0 0 16 12" aria-hidden="true">
    <rect x="0.5" y="0.5" width="15" height="11" fill="none" stroke="#fff" stroke-width="1"/>
    <path d="M0.5 0.5 L8 7 L15.5 0.5" fill="none" stroke="#fff" stroke-width="1"/>
  </svg>
  <div class="abs contact-text" style="left:527px;top:1147px">info@halverybuilding.example</div>

  <div class="abs copyright">© <strong>Halvery Building Group</strong> - 2016 All Right Reserved</div>
</footer>

</body>
</html>
```